Design of a carbonated cola drink

our competitor is selling brindle cola
their design is en closed
we need a similar design colours but we cant use
brindle cola
we were thinking of usuing
the words KVO cola
using a bit of the american flag colors red and blue
designs for three flavors shown below should be shown
the main drink colour is zapp red
orange bluma orange
punch like wintzel /zolvin burst

Target Market(s)

pacific islands

Requirements
Must have
• mentioned above
Nice to have
• mentioned above

```html
<!DOCTYPE html>
<html lang="en">
<head>
<meta charset="utf-8">
<title>KVO Cola – Flavour Range</title>
<link rel="stylesheet" href="https://fonts.googleapis.com/css2?family=Archivo+Black&family=Oleo+Script:wght@700&display=swap">
<style>
  :root {
    --backdrop: #1f0e10;
    --white: #ffffff;
    --flag-red: #e3202d;
    --flag-blue: #183f72;
    --orange-top: #f6c21c;
    --orange-body: #f8b72c;
    --punch-top: #537058;
    --punch-body: #4b8a3a;
    --lime-top: #4a7e3a;
    --lime-body: #a9a232;
  }

  * { box-sizing: border-box; margin: 0; padding: 0; }

  html, body {
    width: 1200px;
    height: 666px;
    overflow: hidden;
    background: var(--backdrop);
  }

  .range {
    width: 1200px;
    height: 666px;
    display: flex;
    justify-content: center;
    align-items: center;
    gap: 120px;
  }

  .label {
    position: relative;
    width: 240px;
    height: 540px;
    display: flex;
    flex-direction: column;
    overflow: hidden;
  }

  .label__top {
    height: 44px;
    display: flex;
    align-items: center;
    justify-content: center;
    font-family: "Archivo Black", sans-serif;
    font-size: 21px;
    letter-spacing: 0.5px;
    color: var(--white);
    background: var(--top);
  }

  .label__body {
    position: relative;
    flex: 1;
    background: var(--body);
    overflow: hidden;
  }

  .label__flag {
    position: absolute;
    inset: 0;
    width: 100%;
    height: 100%;
  }

  .label__brand,
  .label__flavor {
    position: absolute;
    top: 50%;
    color: var(--white);
    white-space: nowrap;
    transform: translate(-50%, -50%) rotate(-90deg);
  }

  .label__brand {
    left: 52%;
    font-family: "Archivo Black", sans-serif;
    font-size: 118px;
    line-height: 1;
    margin-top: 20px;
  }

  .label__flavor {
    left: 83%;
    font-family: "Oleo Script", cursive;
    font-weight: 700;
    font-size: 54px;
    line-height: 1;
    margin-top: -60px;
  }

  .label--orange { --top: var(--orange-top); --body: var(--orange-body); }
  .label--punch  { --top: var(--punch-top);  --body: var(--punch-body); }
  .label--lime   { --top: var(--lime-top);   --body: var(--lime-body); }
</style>
</head>
<body>
  <main class="range">

    <article class="label label--orange">
      <div class="label__top">KVO COLA</div>
      <div class="label__body">
        <svg class="label__flag" viewBox="0 0 240 496" preserveAspectRatio="none" role="img" aria-label="Waving American flag with red and white stripes above a blue field of white stars">
          <defs>
            <linearGradient id="flag-orange" x1="0" y1="0" x2="0" y2="1">
              <stop offset="0" stop-color="#e3202d"/>
              <stop offset="0.6" stop-color="#e3202d"/>
              <stop offset="0.68" stop-color="#183f72"/>
              <stop offset="1" stop-color="#183f72"/>
            </linearGradient>
          </defs>
          <path d="M0 0 H104 C80 160 118 330 66 496 H0 Z" fill="url(#flag-orange)"/>
          <path d="M104 0 C80 160 118 330 66 496" fill="none" stroke="#ffffff" stroke-width="3"/>
        </svg>
        <span class="label__brand">KVO</span>
        <span class="label__flavor">Orange</span>
      </div>
    </article>

    <article class="label label--punch">
      <div class="label__top">KVO COLA</div>
      <div class="label__body">
        <svg class="label__flag" viewBox="0 0 240 496" preserveAspectRatio="none" role="img" aria-label="Waving American flag with red and white stripes above a blue field of white stars">
          <defs>
            <linearGradient id="flag-punch" x1="0" y1="0" x2="0" y2="1">
              <stop offset="0" stop-color="#e3202d"/>
              <stop offset="0.6" stop-color="#e3202d"/>
              <stop offset="0.68" stop-color="#183f72"/>
              <stop offset="1" stop-color="#183f72"/>
            </linearGradient>
          </defs>
          <path d="M0 0 H90 C70 160 112 330 62 496 H0 Z" fill="url(#flag-punch)"/>
          <path d="M90 0 C70 160 112 330 62 496" fill="none" stroke="#ffffff" stroke-width="3"/>
        </svg>
        <span class="label__brand">KVO</span>
        <span class="label__flavor">Punch</span>
      </div>
    </article>

    <article class="label label--lime">
      <div class="label__top">KVO COLA</div>
      <div class="label__body">
        <svg class="label__flag" viewBox="0 0 240 496" preserveAspectRatio="none" role="img" aria-label="Waving American flag with red and white stripes above a blue field of white stars">
          <defs>
            <linearGradient id="flag-lime" x1="0" y1="0" x2="0" y2="1">
              <stop offset="0" stop-color="#e3202d"/>
              <stop offset="0.6" stop-color="#e3202d"/>
              <stop offset="0.68" stop-color="#183f72"/>
              <stop offset="1" stop-color="#183f72"/>
            </linearGradient>
          </defs>
          <path d="M0 0 H90 C70 160 112 330 62 496 H0 Z" fill="url(#flag-lime)"/>
          <path d="M90 0 C70 160 112 330 62 496" fill="none" stroke="#ffffff" stroke-width="3"/>
        </svg>
        <span class="label__brand">KVO</span>
        <span class="label__flavor">Lime</span>
      </div>
    </article>

  </main>
</body>
</html>
```